Maple Cove Laser Dermal Studio needs an 8 page WP redesign

We need a colorful re-design for an 8 page Wordpress website. The current preliminary website is live. The home page URL is http://maplecovelaserdermalstudio.com The new logo is live on the website also. I would like a (re)design using the colors that are represented by the new logo file, and any additional complimentary colors. The information regarding the business can be found on the website already, so please review it for insight. The name of the business is "Maple Cove Laser Dermal Studio".

Target Market(s)

The targeted website viewer is an adult female between the ages of 30 and 75 who is interested in facial renewal, wart removal and scar removal. This website should inspire in the target viewer the benefits of laser facial renewal, wart removal and new scar removal. Potential website viewers are wanting and searching for improved skin health and appearance. The website must represent the essence of a professional spa business.

Industry/Entity Type

Business

Font styles to use
Sans Serif

Requirements
Must have
• - The phone number placed in a visible and high value widget area that allows mobile phone browser dialing.

```html
<!DOCTYPE html>
<html lang="en">
<head>
<meta charset="utf-8">
<title>Maple Cove Laser Dermal Studio</title>
<link href="https://fonts.googleapis.com/css2?family=Open+Sans:wght@400;600;700&family=Roboto+Condensed:wght@400;700&display=swap" rel="stylesheet">
<style>
:root{
  --purple:#a8179f;
  --purple-deep:#8e1488;
  --plum:#5b3a5e;
  --heading:#a0179b;
  --text:#6b6b6b;
  --text-dark:#444;
  --page:#f6f6f6;
  --band:#ececef;
  --promo:#e4ebee;
  --frame:#b9b9b9;
  --white:#fff;
}
*{box-sizing:border-box;margin:0;padding:0}
html,body{width:1200px;height:2410px;overflow:hidden}
body{position:relative;background:var(--page);font-family:"Open Sans",Arial,sans-serif;color:var(--text)}
.abs{position:absolute}
a{color:inherit;text-decoration:none}

/* hero */
.hero{left:0;top:0;width:1200px;height:516px;
  background:linear-gradient(90deg,#c9467f 0%,#b33c95 8%,#e3bfa9 22%,#eed3c0 45%,#b6c9da 62%,#e9cfbd 80%,#b0308f 92%,#8f1f87 100%)}
.brand{left:88px;top:22px;display:flex;align-items:center;gap:10px}
.brand-dot{width:18px;height:18px;border-radius:50%;background:var(--purple)}
.brand-name{font-family:"Roboto Condensed",sans-serif;font-weight:700;font-size:22px;line-height:25px;color:var(--plum);width:220px}
.nav{left:382px;top:45px;display:flex}
.nav a{font-family:"Roboto Condensed",sans-serif;font-size:12.5px;color:var(--white);text-transform:uppercase;padding:7px 9px;letter-spacing:.2px}
.nav a.active{background:var(--purple);position:relative}
.nav a.active::after{content:"";position:absolute;left:50%;bottom:-6px;margin-left:-6px;border:6px solid transparent;border-bottom:0;border-top-color:var(--purple)}

/* section titles */
.title{left:0;width:1200px;text-align:center;font-family:"Roboto Condensed",sans-serif;font-weight:700;font-size:17.5px;color:var(--heading);text-transform:uppercase}
.rule{height:2px;background:#bdbdbd;width:136px;left:532px}

.intro{left:205px;top:590px;width:790px;text-align:center;font-size:10.6px;line-height:19.5px;color:var(--text)}
.round-arrow{left:585px;top:718px;width:30px;height:30px;border-radius:50%;background:var(--purple)}

/* treatments */
.treat{width:188px}
.treat .photo{height:124px}
.treat h3{margin-top:16px;font-family:"Roboto Condensed",sans-serif;font-size:13.5px;color:var(--text-dark);text-transform:uppercase;font-weight:400}
.treat h3.hl{color:var(--heading);font-weight:700}
.treat p{margin-top:7px;font-size:10.5px;line-height:16px}

/* testimonials */
.testi-band{left:0;top:1089px;width:1200px;height:225px;background:var(--band)}
.avatar{left:193px;top:1156px;width:106px;height:106px;border-radius:50%;background:radial-gradient(circle at 50% 45%,#c89a86,#6b4b46 70%,#d8d8d8 72%)}
.quote{left:326px;top:1164px;width:676px;font-size:11.5px;line-height:21px}
.quote .mark{font-family:Georgia,serif;font-size:22px;color:var(--text-dark);line-height:0;vertical-align:-6px}
.testi-name{left:326px;top:1241px;font-weight:600;font-size:14px;color:var(--heading)}
.dots{left:580px;top:1276px;display:flex;gap:6px}
.dots i{width:6px;height:6px;border-radius:50%;background:#b9b9b9}
.dots i.on{background:var(--purple)}

/* blog */
.post{width:178px}
.post .top{display:flex;height:125px}
.post .photo{width:142px;height:125px}
.post .stats{width:36px;background:var(--purple);color:var(--white);font-size:9.5px;display:flex;flex-direction:column;align-items:center;padding-top:14px;gap:6px}
.post h4{margin-top:13px;font-size:11.5px;font-weight:600;color:var(--text-dark)}
.post h4.hl{color:var(--heading)}
.post p{margin-top:6px;font-size:10px;line-height:16px;color:#8a8a8a}
.post .more{margin-top:14px;display:flex;align-items:center;gap:10px;font-size:8px;text-transform:uppercase;color:#aaa}
.post .more span.line{flex:1;height:1px;background:#ccc}
.post .more.hl{color:var(--heading)}
.post .more.hl span.line{background:var(--purple);height:2px}

/* promo */
.promo{left:193px;top:1645px;width:814px;height:265px;background:var(--promo)}
.promo-photo{left:193px;top:1645px;width:233px;height:265px;background:linear-gradient(90deg,#e8d3c3,#f0dccd 60%,#e4ebee)}
.promo-title{left:440px;top:1658px;font-family:"Roboto Condensed",sans-serif;font-weight:400;font-size:33px;line-height:40px;color:var(--heading);text-transform:uppercase;letter-spacing:-.2px}
.promo-sub{left:440px;top:1704px;width:560px;text-align:center;font-size:16px;color:var(--text-dark)}
.promo-lead{left:440px;top:1738px;width:560px;text-align:center;font-size:11.5px;font-weight:700;color:var(--text-dark)}
.promo-end{left:440px;top:1766px;width:408px;text-align:center;font-size:16.5px;font-weight:700;color:var(--heading)}
.deal{top:1807px;width:111px;height:88px;background:var(--purple);color:var(--white);padding:8px 8px 0 9px}
.deal .num{font-size:34px;font-weight:700;line-height:34px;float:left;margin-right:4px}
.deal .lbl{font-size:12.5px;line-height:15px;padding-top:3px}
.deal .price{clear:both;padding-top:8px;font-size:14px;font-weight:700}
.call{left:809px;top:1807px;width:151px;height:88px;background:var(--plum);color:var(--white);padding:8px 10px}
.call b{display:block;text-align:center;font-size:14.5px}
.call a{display:block;text-align:center;font-weight:700;font-size:14.5px}
.call small{display:block;font-size:9px;line-height:13px;margin-top:4px}
.agent{left:958px;top:1775px;width:49px;height:120px;background:linear-gradient(180deg,#d9b4a0,#8fd3df 60%,#bfe8ef);border-radius:24px 24px 0 0}

/* before after */
.ba-arrow{top:2038px;width:30px;height:30px;border-radius:50%;background:var(--purple)}
.ba{top:1991px;width:232px;height:122px;background:var(--frame);padding:7px 16px}
.ba .inner{display:flex;height:108px;position:relative}
.ba .inner div{flex:1}
.ba .tags{position:absolute;left:50%;bottom:8px;transform:translateX(-50%);display:flex;font-size:7.5px;font-weight:700;text-transform:uppercase}
.ba .tags span{padding:2px 6px}
.ba .tags .b{background:#222;color:#fff}
.ba .tags .a{background:#fff;color:#222}

/* footer */
.f-col h5{font-family:"Roboto Condensed",sans-serif;font-size:15px;font-weight:700;color:var(--heading);text-transform:uppercase;padding-bottom:8px;border-bottom:1px solid #bbb}
.links{display:grid;grid-template-columns:114px 100px;row-gap:11.2px;margin-top:14px;font-size:10px;color:var(--text-dark)}
.links a::before{content:"→ ";color:var(--text-dark)}
.links a.on{color:var(--heading)}
.news{display:flex;gap:10px;margin-top:14px;font-size:10px;line-height:17px}
.field{width:200px;height:28px;border:1px solid #d6d6d6;background:#fff;font-size:9.5px;color:#aaa;font-style:italic;padding:7px 9px;margin-top:6px}
.btn{display:inline-block;margin-top:18px;width:85px;height:29px;line-height:29px;text-align:center;background:var(--purple);color:#fff;font-size:11.5px}
.contact{margin-top:12px;font-size:9.8px;line-height:17px;color:var(--text-dark)}
.contact .row{display:flex;gap:12px;align-items:flex-start;margin-bottom:17px}
.contact svg{flex:none}
.bottom{left:0;top:2362px;width:1200px;height:48px;background:var(--purple)}
.copy{left:193px;top:2378px;font-size:10.5px;color:#fff}
.social{top:2372px;width:28px;height:28px;border:1.5px solid rgba(255,255,255,.85);border-radius:50%}
</style>
</head>
<body>

<header>
  <div class="abs hero" role="img" aria-label="Photo of a woman relaxing during a facial massage, framed by pink and violet tones"></div>
  <div class="abs brand"><span class="brand-dot"></span><span class="brand-name">Maple Cove Laser Dermal Studio</span></div>
  <nav class="abs nav">
    <a class="active" href="#">Home</a><a href="#">About Us</a><a href="#">Skin Renewal</a><a href="#">Scar Removal</a><a href="#">Wart Removal</a><a href="#">Your Visit</a><a href="#">Blog</a><a href="#">Contact Us</a>
  </nav>
</header>

<section>
  <h2 class="abs title" style="top:544px">Have you considered laser skin renewal therapy?</h2>
  <div class="abs rule" style="top:575px"></div>
  <p class="abs intro">You will truly love laser skin renewal if your skin is showing signs of premature aging or the skin has sustained sun damage. Conditions such as excessive redness due to sun exposure or fine lines will be concerns of the past. In fact, laser skin therapy is a unique and innovative way to enjoy youthful and healthy skin without resorting to painful and inconvenient surgery. Both men and women are receiving benefits from laser skin therapy.<br>The literature contains ample scientific evidence to support laser skin renewal. After this therapy, your skin will produce collagen, which reduces and minimizes the appearance of fine lines and wrinkles. Imagine getting all this with minimal pain and no downtime? Doesn't it make you feel like getting in touch with our laser skin specialist today?</p>
  <svg class="abs round-arrow" viewBox="0 0 30 30"><path d="M13 9l6 6-6 6" fill="none" stroke="#fff" stroke-width="3"/></svg>
</section>

<section>
  <h2 class="abs title" style="top:777px">Number of treatments</h2>
  <div class="abs rule" style="top:810px"></div>
  <div class="abs treat" style="left:193px;top:853px">
    <div class="photo" role="img" aria-label="Photo of a facial massage treatment" style="background:linear-gradient(135deg,#f2d6c2,#e6b79b)"></div>
    <h3 class="hl">Laser skin therapy</h3>
    <p>Lorem ipsum dolor sit amet, consecr adipiscing elit. Maecenas bibendum</p>
  </div>
  <div class="abs treat" style="left:398px;top:853px">
    <div class="photo" role="img" aria-label="Portrait photo of a woman with glowing skin" style="background:linear-gradient(135deg,#3a1c4e,#8a5a8c 55%,#2a1436)"></div>
    <h3>Skin renewal</h3>
    <p>Lorem ipsum dolor sit amet, consecr adipiscing elit. Maecenas bibendum</p>
  </div>
  <div class="abs treat" style="left:604px;top:853px">
    <div class="photo" role="img" aria-label="Photo of a woman relaxing at a spa with candles" style="background:linear-gradient(135deg,#6b3b1c,#d8a47a 55%,#f1e3d2)"></div>
    <h3>Scar removal</h3>
    <p>Lorem ipsum dolor sit amet, consecr adipiscing elit. Maecenas bibendum</p>
  </div>
  <div class="abs treat" style="left:809px;top:853px">
    <div class="photo" role="img" aria-label="Portrait photo of a woman touching her cheek" style="background:linear-gradient(135deg,#d8a25c,#f2e1cf 55%,#e9cdb8)"></div>
    <h3>Wart removal</h3>
    <p>Lorem ipsum dolor sit amet, consecr adipiscing elit. Maecenas bibendum</p>
  </div>
</section>

<section>
  <div class="abs testi-band"></div>
  <h2 class="abs title" style="top:1119px">Testimonials</h2>
  <div class="abs rule" style="top:1152px"></div>
  <div class="abs avatar" role="img" aria-label="Round portrait photo of a client"></div>
  <p class="abs quote"><span class="mark">“</span> Lorem ipsum dolor sit amet, consectetur adipiscing elit. Maecenas nunc ex, dictum nec ipsum vel, vulputate luctus nisl. Nunc nec metus cursus, dignissim nunc sed, porta urna. Pellentesque scelerisque seullamcor rhoncus. Cras volutpat turpis vel sem pharetra, at pellentesque metus ullamcorper. <span class="mark">”</span></p>
  <div class="abs testi-name">Mark Lorem ispum</div>
  <div class="abs dots"><i class="on"></i><i></i><i></i></div>
</section>

<section>
  <h2 class="abs title" style="top:1342px">Latest blog</h2>
  <div class="abs rule" style="top:1375px"></div>
  <article class="abs post" style="left:193px;top:1394px">
    <div class="top"><div class="photo" role="img" aria-label="Photo of a woman holding an apple" style="background:linear-gradient(135deg,#5a3a2e,#e7c4ad 60%,#f4f0ea)"></div>
      <div class="stats"><svg width="11" height="10" viewBox="0 0 12 11"><path d="M6 10L1 5a3 3 0 0 1 5-3 3 3 0 0 1 5 3z" fill="#fff"/></svg>126<svg width="11" height="10" viewBox="0 0 12 11"><path d="M1 1h10v6H5l-3 3V7H1z" fill="#fff"/></svg>235</div></div>
    <h4 class="hl">Lorem ipsum dolor sit amet</h4>
    <p>Consectetur adipis Maecenas aliquet velit in lacus porta.</p>
    <div class="more hl">Read more<span class="line"></span></div>
  </article>
  <article class="abs post" style="left:405px;top:1394px">
    <div class="top"><div class="photo" role="img" aria-label="Photo of a smiling woman at the beach" style="background:linear-gradient(135deg,#7fc6e0,#d9b093 55%,#f1dac8)"></div>
      <div class="stats"><svg width="11" height="10" viewBox="0 0 12 11"><path d="M6 10L1 5a3 3 0 0 1 5-3 3 3 0 0 1 5 3z" fill="#fff"/></svg>126<svg width="11" height="10" viewBox="0 0 12 11"><path d="M1 1h10v6H5l-3 3V7H1z" fill="#fff"/></svg>235</div></div>
    <h4>Lorem ipsum dolor sit amet</h4>
    <p>Consectetur adipis Maecenas aliquet velit in lacus porta.</p>
    <div class="more">Read more<span class="line"></span></div>
  </article>
  <article class="abs post" style="left:617px;top:1394px">
    <div class="top"><div class="photo" role="img" aria-label="Photo of a woman wearing a crown of red flowers" style="background:linear-gradient(180deg,#d8262a,#eec9b3 55%,#f3f3f3)"></div>
      <div class="stats"><svg width="11" height="10" viewBox="0 0 12 11"><path d="M6 10L1 5a3 3 0 0 1 5-3 3 3 0 0 1 5 3z" fill="#fff"/></svg>126<svg width="11" height="10" viewBox="0 0 12 11"><path d="M1 1h10v6H5l-3 3V7H1z" fill="#fff"/></svg>235</div></div>
    <h4>Lorem ipsum dolor sit amet</h4>
    <p>Consectetur adipis Maecenas aliquet velit in lacus porta.</p>
    <div class="more">Read more<span class="line"></span></div>
  </article>
  <article class="abs post" style="left:829px;top:1394px">
    <div class="top"><div class="photo" role="img" aria-label="Photo of a woman with long dark hair" style="background:linear-gradient(135deg,#8b7a6e,#d6b29b 55%,#4a3228)"></div>
      <div class="stats"><svg width="11" height="10" viewBox="0 0 12 11"><path d="M6 10L1 5a3 3 0 0 1 5-3 3 3 0 0 1 5 3z" fill="#fff"/></svg>126<svg width="11" height="10" viewBox="0 0 12 11"><path d="M1 1h10v6H5l-3 3V7H1z" fill="#fff"/></svg>235</div></div>
    <h4>Lorem ipsum dolor sit amet</h4>
    <p>Consectetur adipis Maecenas aliquet velit in lacus porta.</p>
    <div class="more">Read more<span class="line"></span></div>
  </article>
</section>

<section>
  <div class="abs promo"></div>
  <div class="abs promo-photo" role="img" aria-label="Photo of a woman with smooth youthful skin"></div>
  <h2 class="abs promo-title">New years resolution special!</h2>
  <p class="abs promo-sub">Restore your youthful skin this year!</p>
  <p class="abs promo-lead">Take advantage of our laser skin renewal specials for single or multiple sessions at low pricing.</p>
  <p class="abs promo-end">Special ENDS January 3, 2015 at 5:00 PM.</p>
  <div class="abs deal" style="left:429px"><span class="num">1</span><div class="lbl">Single<br>Session</div><div class="price">Deal - $199</div></div>
  <div class="abs deal" style="left:556px"><span class="num">3</span><div class="lbl">Sessions<br>Package</div><div class="price">Deal - $459</div></div>
  <div class="abs deal" style="left:683px"><span class="num">6</span><div class="lbl">Sessions<br>Package</div><div class="price">Deal - $899</div></div>
  <div class="abs call"><b>CALL US</b><a href="tel:+15552147730">555-214-7730</a><small>To schedule your<br>Confirm appointment</small></div>
  <div class="abs agent" role="img" aria-label="Photo of a receptionist wearing a headset"></div>
</section>

<section>
  <h2 class="abs title" style="top:1938px">Skin care before and after</h2>
  <svg class="abs ba-arrow" style="left:192px" viewBox="0 0 30 30"><path d="M17 9l-6 6 6 6" fill="none" stroke="#fff" stroke-width="3"/></svg>
  <div class="abs ba" style="left:239px"><div class="inner" role="img" aria-label="Before and after photos of a client's skin treatment"><div style="background:linear-gradient(135deg,#3a2b26,#e6cdbd)"></div><div style="background:linear-gradient(135deg,#e9d6c8,#3a2b26)"></div>
    <div class="tags"><span class="b">Before</span><span class="a">After</span></div></div></div>
  <div class="abs ba" style="left:487px"><div class="inner" role="img" aria-label="Before and after photos of a client's scar removal"><div style="background:linear-gradient(135deg,#d7b07a,#e2c2aa)"></div><div style="background:linear-gradient(135deg,#e3c59a,#e9cfbd)"></div>
    <div class="tags"><span class="b">Before</span><span class="a">After</span></div></div></div>
  <div class="abs ba" style="left:734px"><div class="inner" role="img" aria-label="Before and after photos of a client's skin renewal"><div style="background:linear-gradient(135deg,#3d2620,#c9927f)"></div><div style="background:linear-gradient(135deg,#45281f,#e2bca7)"></div>
    <div class="tags"><span class="b">Before</span><span class="a">After</span></div></div></div>
  <svg class="abs ba-arrow" style="left:976px" viewBox="0 0 30 30"><path d="M13 9l6 6-6 6" fill="none" stroke="#fff" stroke-width="3"/></svg>
</section>

<footer>
  <div class="abs f-col" style="left:193px;top:2140px;width:200px">
    <h5>Maple Cove</h5>
    <div class="links">
      <a class="on" href="#">Home</a><a href="#">Blog</a>
      <a href="#">About Us</a><a href="#">Warranty and</a>
      <a href="#">Skin Renewal</a><a href="#">Customer care</a>
      <a href="#">Scar Removal</a><a href="#">Privacy Policy</a>
      <a href="#">Wart Removal</a><a href="#">Suggestions</a>
      <a href="#">Your Visit</a><a href="#">Contact Us</a>
    </div>
  </div>
  <div class="abs f-col" style="left:495px;top:2140px;width:200px">
    <h5>Newsletter</h5>
    <div class="news"><svg width="26" height="20" viewBox="0 0 26 20"><rect x="1" y="3" width="24" height="16" fill="var(--purple)"/><path d="M1 3l12 9 12-9" fill="none" stroke="#fff" stroke-width="1.5"/></svg><span>Sign up with your name and email toget updates fresh updates.</span></div>
    <div class="field">Your Name</div>
    <div class="field">Email Address</div>
    <span class="btn">Subscribe</span>
  </div>
  <div class="abs f-col" style="left:784px;top:2140px;width:225px">
    <h5>Get in touch</h5>
    <div class="contact" style="width:250px">
      <div class="row"><svg width="28" height="24" viewBox="0 0 28 24"><path d="M14 1L1 12h4v11h7v-7h4v7h7V12h4z" fill="var(--purple)"/></svg><span>Harbor Point Medical Plaza 2420 Lakeview Rd,<br>Suite 210 Maple Cove, TX 77590</span></div>
      <div class="row"><svg width="28" height="20" viewBox="0 0 28 20"><path d="M7 1c2 0 3 4 2 5l-2 2c1 3 4 6 7 7l2-2c1-1 5 0 5 2v3c0 1-1 2-3 2C9 20 3 12 3 4 3 2 4 1 5 1z" fill="var(--purple)"/></svg><a href="tel:+15552147730">555-214-7730</a></div>
      <div class="row"><svg width="28" height="20" viewBox="0 0 28 20"><rect x="8" y="1" width="12" height="5" fill="var(--purple)"/><rect x="4" y="6" width="20" height="9" fill="var(--purple)"/><rect x="8" y="12" width="12" height="7" fill="#fff" stroke="var(--purple)" stroke-width="2"/></svg><span>555-214-7730</span></div>
      <div class="row"><svg width="28" height="18" viewBox="0 0 28 18"><rect x="3" y="1" width="22" height="16" fill="var(--purple)"/><path d="M3 1l11 9 11-9" fill="none" stroke="#fff" stroke-width="1.5"/></svg><span>info@maplecovelaserdermalstudio.com</span></div>
    </div>
  </div>

  <div class="abs bottom"></div>
  <p class="abs copy">Copyright &nbsp;20145 Maple Cove Laser Dermal Studio. All right reserved.</p>
  <span class="abs social" style="left:877px"></span>
  <span class="abs social" style="left:913px"></span>
  <span class="abs social" style="left:947px"></span>
  <span class="abs social" style="left:982px"></span>
</footer>

</body>
</html>
```